Hello,
We’re looking for a new WordPress website for Gather Your Light, our company offering unique well-being retreats and workshops.
We currently have a website online (you can consult it : www.gatheryourlight.ch), but we now need to build a new site on WordPress — more flexible, more intuitive to manage, and better aligned with our evolving needs.

What we’re looking for:
A new userfriendly WordPress site, with:
Inspiring, elegant, and modern design
Smooth user experience on desktop and mobile
Innovative design proposals – we want to be inspired !
SEO best practices
Respect of our existing color palette
The final website will need to be set up on our existing hosting provider (details can be shared later)

Pages to Include:
- Home
- Our Story
- Our Stays - with links to 5 individual pages, each describing one of our stays in detail.
- Activities – with potential links to individual descriptive pages
- Agenda
- Our Charter
- The Team
- Contact
- Blog

Required Features:
- Space for photos and videos
- Sections for testimonials and press articles
- Blog/article layout with strong readability
- Easy-to-update backend for future content
- Newsletter sign-up (pop-up and in footer)
- Additional pop-up on/off
- “Request info” buttons
- “Booking request” buttons
- Integration of our 4 pillars - Breathe · Feel · Connect · Experience - in the design (They’re currently in the footer, but we’re open to creative suggestions)

Who we are :
Gather Your Light offers well-being and personal growth stays but with a very different spirit.
We’re not a classic wellness brand. Our approach is professional, joyful, and grounded.
We create spaces where people can take a real break — breathe, slow down, and reconnect with themselves.
During our stays, people are welcomed like friends:
with warmth, respect, and no pressure.
Each program combines practices like breathwork, movement, creativity, coaching, and massages in a relaxed, beautiful setting of the French Alps.
What makes us different:
A friendly and down-to-earth atmosphere
A wide mix of activities.
A mix of inner work and simple pleasures
Private rooms, nourishing food, and shared moments
Time to talk, to laugh, to walk, or just be silent together - and feel free to be yourself
Our guests come to pause.
They leave feeling lighter, aligned, and full of life

```html
<!DOCTYPE html>
<html lang="en">
<head>
<meta charset="utf-8">
<title>Gather Your Light – Well-being Retreats</title>
<link rel="stylesheet" href="https://fonts.googleapis.com/css2?family=Arimo:ital,wght@0,400;0,700;1,400&family=Fredoka:wght@500;600&family=Oswald:wght@700&family=Pacifico&display=swap">
<style>
:root{
  --navy:#16298a;
  --navy-deep:#112478;
  --teal:#5ab8ab;
  --teal-dark:#3fa596;
  --olive:#7d8770;
  --grey-bg:#f0f0f0;
  --text:#3a3a3a;
  --muted:#666;
  --gold:#f2b928;
  --white:#fff;
}
*{margin:0;padding:0;box-sizing:border-box}
html,body{width:1200px;height:5164px;overflow:hidden}
body{position:relative;font-family:"Arimo",Arial,sans-serif;color:var(--text);background:var(--white)}
.abs{position:absolute}
.script{font-family:"Pacifico",cursive;color:var(--teal);font-size:19px;line-height:1}
.heading{font-family:"Fredoka",sans-serif;font-weight:600;color:var(--navy);letter-spacing:2px;line-height:1}
.center{left:0;width:1200px;text-align:center}
.btn{position:absolute;display:flex;align-items:center;justify-content:center;background:var(--navy);color:#fff;font-weight:700;font-size:13px;letter-spacing:.5px;border-radius:20px}
.photo{position:absolute}
.arrow{position:absolute;width:30px;height:30px;border-radius:50%;display:flex;align-items:center;justify-content:center}

/* hero */
.hero{position:absolute;left:0;top:0;width:1200px;height:680px;overflow:hidden}
.hero-photo{left:0;top:0;width:1200px;height:680px;background:linear-gradient(100deg,#c9c4bd 0%,#b9b3aa 22%,#cfd8de 45%,#dde6ea 70%,#e6eced 100%)}
.topbar{left:555px;top:0;width:545px;height:36px;background:var(--navy);border-radius:0 0 0 22px;color:#fff;font-size:13px;display:flex;align-items:center;gap:80px;padding-left:48px}
.topbar b{font-weight:700}
.brand{left:110px;top:30px;font-family:"Fredoka",sans-serif;font-weight:600;font-size:27px;color:var(--navy);display:flex;align-items:center;gap:10px}
.brand i{width:14px;height:14px;border-radius:50%;background:var(--teal);display:block}
.nav{left:549px;top:54px;display:flex;gap:0;font-size:14px;font-weight:700;color:#333}
.nav span{margin-right:38px}
.nav .active{color:var(--teal)}
.hero-title{left:495px;top:228px;width:580px;text-align:center;font-family:"Fredoka",sans-serif;font-weight:600;line-height:1;letter-spacing:3px}
.hero-title .l1{display:block;font-size:68px;color:var(--navy)}
.hero-title .l2{display:block;font-size:66px;color:var(--teal);margin-top:20px}
.dots{left:783px;top:545px;display:flex;gap:7px}
.dots i{width:11px;height:11px;border-radius:50%;background:#fff;display:block}
.dots i:first-child{background:#222}

/* about */
.about-text{left:110px;top:847px;width:465px;font-size:15px;line-height:26px;text-align:justify;color:#444}
.about-text p{margin-bottom:26px}
.about-text strong{color:#222}

/* services */
.services{left:0;top:1330px;width:1200px;height:845px;background:var(--grey-bg)}
.card{position:absolute;top:1570px;width:298px;height:485px;background:#fff;border-radius:150px;text-align:center;box-shadow:0 2px 10px rgba(0,0,0,.04)}
.card.featured{border:3px solid #3c3a2e}
.card .photo{left:39px;top:32px;width:220px;height:220px;border-radius:50%}
.card h3{position:absolute;left:30px;width:238px;top:268px;font-size:17px;line-height:26px;color:#222}
.card p{position:absolute;left:38px;width:222px;top:355px;font-size:12.5px;line-height:21px;color:#444}

/* testimonials */
.testimonials{left:0;top:2175px;width:1200px;height:570px;background:linear-gradient(180deg,#142b8d 0%,#16298a 70%,#1e3a98 100%)}
.t-card{position:absolute;top:2398px;width:407px;height:237px;background:#fff;border-radius:4px}
.avatar{position:absolute;left:-45px;top:10px;width:86px;height:86px;border-radius:50%;border:4px solid #fff;box-shadow:0 0 0 1px #ddd}
.t-card .name{position:absolute;left:52px;top:20px;font-size:16px;font-weight:700;color:#222}
.t-card .role{position:absolute;left:52px;top:41px;font-size:12px;color:#555}
.t-card .stars{position:absolute;left:52px;top:73px;color:var(--gold);font-size:15px;letter-spacing:2px}
.t-card .quote{position:absolute;left:52px;top:105px;width:290px;font-style:italic;font-size:16px;line-height:25px;color:#555}
.t-card .qmark{position:absolute;right:38px;bottom:-32px;font-family:Georgia,serif;font-weight:700;font-size:90px;line-height:1;color:var(--teal)}

/* blog */
.post{position:absolute;top:2983px;width:305px}
.post .photo{position:relative;width:305px;height:195px;border-radius:40px 0 40px 0}
.post h3{font-size:19px;line-height:25px;color:#222;margin-top:12px}
.post .date{font-size:14px;color:#555;margin-top:8px;display:flex;align-items:center;gap:8px}
.post p{font-size:12px;line-height:21px;color:#555;margin-top:8px}

/* pillars */
.pillars{left:0;top:3440px;width:1200px;height:575px;background:linear-gradient(120deg,#52b3a6 0%,#64bfb2 50%,#5ab8ab 100%)}
.pillar{position:absolute;top:3640px;width:270px;height:270px;border-radius:50%;background:rgba(255,255,255,.55)}
.pillar .inner{position:absolute;left:22px;top:22px;width:226px;height:226px;border-radius:50%;background:#fff;text-align:center}
.pillar svg{position:absolute;left:63px;top:42px}
.pillar span{position:absolute;left:0;width:226px;top:154px;font-size:20px;font-weight:700;color:#222}

/* contact */
.contact{left:0;top:4015px;width:1200px;height:730px;background:var(--grey-bg)}
.info-icon{position:absolute;left:112px;width:76px;height:76px;border-radius:50%;background:var(--navy);display:flex;align-items:center;justify-content:center}
.info-label{position:absolute;left:210px;font-size:20px;font-weight:700;color:#333}
.info-text{position:absolute;left:210px;font-size:14px;line-height:25px;color:#555}
.field{position:absolute;background:#fff;border:1px solid #c9c9c9;border-radius:3px;font-size:13px;color:#555;padding:20px 0 0 20px}

/* footer */
.footer{left:0;top:4740px;width:1200px;height:424px;background:var(--navy-deep)}
.f-brand{left:145px;top:4855px;font-family:"Fredoka",sans-serif;font-weight:600;font-size:26px;color:#fff;display:flex;align-items:center;gap:10px}
.f-brand i{width:13px;height:13px;border-radius:50%;background:var(--teal);display:block}
.f-head{font-size:19px;font-weight:700;color:#fff}
.f-links{left:490px;top:4895px;list-style:none;font-size:13.5px;color:#fff}
.f-links li{height:26px;line-height:26px}
.f-links li::before{content:"»";margin-right:14px}
</style>
</head>
<body>

<!-- HERO -->
<header class="hero">
  <div class="photo hero-photo abs" role="img" aria-label="Woman with closed eyes breathing in soft morning light, with a dandelion drifting in the sky"></div>
  <div class="abs topbar"><span>&#9990; Call Us : <b>+41 22 555 01 20</b></span><span>&#9993; Mail Us : <b>info@gatheryourlight.ch</b></span></div>
  <div class="abs brand"><i></i>Gather Your Light</div>
  <nav class="abs nav">
    <span class="active">Home</span><span>About</span><span>Services</span><span>Reviews</span><span>Blog</span><span>Contact</span>
    <svg width="14" height="14" viewBox="0 0 14 14" style="margin-top:2px"><circle cx="6" cy="6" r="4.5" fill="none" stroke="#333" stroke-width="2"/><line x1="9.3" y1="9.3" x2="13" y2="13" stroke="#333" stroke-width="2"/></svg>
  </nav>
  <h1 class="abs hero-title"><span class="l1">GATHER</span><span class="l2">YOUR LIGHT</span></h1>
  <div class="btn" style="left:740px;top:400px;width:156px;height:37px;">GET STARTED</div>
  <div class="abs dots"><i></i><i></i><i></i><i></i></div>
  <svg class="abs" style="left:0;top:560px" width="1200" height="120" viewBox="0 0 1200 120">
    <path d="M0 60 C 150 35, 330 20, 520 50 C 700 75, 900 75, 1200 55 L1200 120 L0 120 Z" fill="var(--navy)"/>
    <path d="M0 60 C 150 40, 300 10, 480 55 C 640 95, 900 115, 1200 115 L1200 120 L0 120 Z" fill="#fff"/>
  </svg>
</header>

<!-- ABOUT -->
<section class="about">
  <div class="abs script" style="left:110px;top:735px;font-size:18px">Gather Your Light</div>
  <h2 class="abs heading" style="left:110px;top:768px;font-size:36px">ABOUT US</h2>
  <svg class="abs" style="left:110px;top:810px" width="145" height="12" viewBox="0 0 145 12"><path d="M2 9 C 40 1, 100 1, 143 8 C 100 6, 45 6, 2 9 Z" fill="var(--navy)"/></svg>
  <div class="abs about-text">
    <p>Gather Your Light offers well-being and personal growth stays but with a very different spirit. We’re not a classic wellness brand. Our approach is professional, joyful, and grounded. We create spaces where people can take a real break — breathe, slow down, and reconnect with themselves.</p>
    <p><strong>During our stays, people are welcomed like friends:</strong></p>
    <p>with warmth, respect, and no pressure. Each program combines practices like breathwork, movement, creativity, coaching, and massages in a relaxed, beautiful setting of the French Alps.</p>
  </div>
  <div class="btn" style="left:110px;top:1180px;width:158px;height:38px;">LEARN MORE</div>
  <div class="photo" style="left:630px;top:735px;width:465px;height:465px;border-radius:50%;background:#c9c9cd"></div>
  <div class="photo" role="img" aria-label="Warm wooden chalet living room with a black hanging fireplace and yellow armchair" style="left:641px;top:746px;width:443px;height:443px;border-radius:50%;background:radial-gradient(circle at 40% 40%,#b58a5e 0%,#7a5536 45%,#3b2c23 80%)"></div>
  <div class="photo" style="left:623px;top:1068px;width:166px;height:166px;border-radius:50%;background:#fff"></div>
  <div class="photo" role="img" aria-label="Alpine meadow with a red sculpture under mountains" style="left:629px;top:1074px;width:154px;height:154px;border-radius:50%;background:linear-gradient(180deg,#a9b9c9 0%,#8c9a8c 45%,#4f7a3a 70%,#3f6a2e 100%)"></div>
</section>

<!-- SERVICES -->
<section class="abs services"></section>
<div class="abs script center" style="top:1446px;font-size:18px">Our Services</div>
<h2 class="abs heading center" style="top:1475px;font-size:37px">WHAT DO WE HAVE TO OFFER?</h2>
<svg class="abs" style="left:500px;top:1520px" width="200" height="14" viewBox="0 0 200 14"><path d="M2 10 C 60 1, 140 1, 198 9 C 140 7, 60 7, 2 10 Z" fill="var(--navy)"/></svg>
<div class="arrow" style="left:41px;top:1772px;background:var(--olive)"><svg width="10" height="10" viewBox="0 0 10 10"><path d="M6.5 1.5 L3 5 L6.5 8.5" fill="none" stroke="#fff" stroke-width="1.6"/></svg></div>
<div class="arrow" style="left:1128px;top:1772px;background:var(--olive)"><svg width="10" height="10" viewBox="0 0 10 10"><path d="M3.5 1.5 L7 5 L3.5 8.5" fill="none" stroke="#fff" stroke-width="1.6"/></svg></div>
<article class="card" style="left:112px">
  <div class="photo" role="img" aria-label="Bright private bedroom with white bedding" style="background:linear-gradient(160deg,#d8d8d8 0%,#a6a6a6 50%,#e9e9e9 100%)"></div>
  <h3>A friendly and down-to-earth atmosphere</h3>
  <p>Lorem ipsum dolor sit amet, conse ctetur adipiscing elit, sed do eius dolore magna aliqua.</p>
</article>
<article class="card featured" style="left:450px">
  <div class="photo" role="img" aria-label="Woman stretching her arms forward during a group movement class" style="left:36px;top:29px;background:linear-gradient(160deg,#e6e2dc 0%,#c8a68a 55%,#b0704a 100%)"></div>
  <h3 style="left:27px">A wide mix<br>of activities.</h3>
  <p style="left:35px;top:352px">Lorem ipsum dolor sit amet, conse ctetur adipiscing elit, sed do eius dolore magna aliqua.</p>
</article>
<article class="card" style="left:790px">
  <div class="photo" role="img" aria-label="Woman sitting cross-legged in meditation in a calm room" style="background:linear-gradient(160deg,#6b4a33 0%,#a7795a 50%,#4d5b78 100%)"></div>
  <h3>A mix of inner work and simple pleasures</h3>
  <p>Lorem ipsum dolor sit amet, conse ctetur adipiscing elit, sed do eius dolore magna aliqua.</p>
</article>

<!-- TESTIMONIALS -->
<section class="abs testimonials"></section>
<div class="abs script center" style="top:2258px;font-size:18px;color:#fff">Testimonials</div>
<h2 class="abs center" style="top:2292px;font-family:'Oswald',sans-serif;font-weight:700;font-size:36px;color:#fff;line-height:1">WHAT OUR CLIENTS SAY</h2>
<svg class="abs" style="left:500px;top:2342px" width="200" height="14" viewBox="0 0 200 14"><path d="M2 10 C 60 1, 140 1, 198 9 C 140 7, 60 7, 2 10 Z" fill="#fff"/></svg>
<div class="arrow" style="left:41px;top:2492px;background:#8a8fa8"><svg width="10" height="10" viewBox="0 0 10 10"><path d="M6.5 1.5 L3 5 L6.5 8.5" fill="none" stroke="#fff" stroke-width="1.6"/></svg></div>
<div class="arrow" style="left:1128px;top:2492px;background:#8a8fa8"><svg width="10" height="10" viewBox="0 0 10 10"><path d="M3.5 1.5 L7 5 L3.5 8.5" fill="none" stroke="#fff" stroke-width="1.6"/></svg></div>
<article class="t-card" style="left:170px">
  <div class="avatar" role="img" aria-label="Portrait of a guest" style="background:linear-gradient(160deg,#e3c2a8,#b5825e)"></div>
  <div class="name">Lena Morel</div>
  <div class="role">Fitness Enthusiast</div>
  <div class="stars">★★★★★</div>
  <p class="quote">Lorem ipsum dolor sit amet, cons ectetur adipiscing elit, sed do eius mod tempor incididunt ut labo re et dolore magna aliqua.</p>
  <div class="qmark">“</div>
</article>
<article class="t-card" style="left:660px">
  <div class="avatar" role="img" aria-label="Portrait of a guest" style="background:linear-gradient(160deg,#d9d9d9,#6e6e6e)"></div>
  <div class="name">Paul Varga</div>
  <div class="role">Retired Veteran</div>
  <div class="stars">★★★★★</div>
  <p class="quote">Lorem ipsum dolor sit amet, cons ectetur adipiscing elit, sed do eius mod tempor incididunt ut labo re et dolore magna aliqua.</p>
  <div class="qmark">“</div>
</article>

<!-- BLOG -->
<div class="abs script center" style="top:2823px;font-size:18px">Our Blog</div>
<h2 class="abs heading center" style="top:2852px;font-size:40px">LATEST ARTICLES</h2>
<svg class="abs" style="left:500px;top:2900px" width="200" height="14" viewBox="0 0 200 14"><path d="M2 10 C 60 1, 140 1, 198 9 C 140 7, 60 7, 2 10 Z" fill="var(--navy)"/></svg>
<p class="abs center" style="top:2936px;font-size:19px;color:#444">Discover the dedicated professionals committed to your health.</p>
<div class="arrow" style="left:41px;top:3145px;background:var(--olive)"><svg width="10" height="10" viewBox="0 0 10 10"><path d="M6.5 1.5 L3 5 L6.5 8.5" fill="none" stroke="#fff" stroke-width="1.6"/></svg></div>
<div class="arrow" style="left:1128px;top:3145px;background:var(--olive)"><svg width="10" height="10" viewBox="0 0 10 10"><path d="M3.5 1.5 L7 5 L3.5 8.5" fill="none" stroke="#fff" stroke-width="1.6"/></svg></div>
<article class="post" style="left:110px">
  <div class="photo" role="img" aria-label="Glass water dispenser with soft bokeh lights" style="background:linear-gradient(160deg,#4a5a70 0%,#8aa4c0 50%,#c9d7e6 100%)"></div>
  <h3>Lorem ipsum dolor sit amet, consectetur</h3>
  <div class="date"><svg width="14" height="14" viewBox="0 0 14 14"><rect x="1" y="2.5" width="12" height="10.5" rx="1.5" fill="var(--navy)"/><rect x="2.5" y="6" width="9" height="5.5" fill="#fff"/><rect x="3.5" y="0.5" width="1.6" height="3.5" fill="var(--navy)"/><rect x="8.9" y="0.5" width="1.6" height="3.5" fill="var(--navy)"/></svg>Jun 25,2025</div>
  <p>Lorem ipsum dolor sit amet, consectetur adipi scing elit, sed do eiusmod tempor incididunt ut labore et dolore magna aliqua.</p>
</article>
<article class="post" style="left:447px">
  <div class="photo" role="img" aria-label="Colourful plated dish with flowers on a yellow sauce" style="background:linear-gradient(160deg,#5d7a4e 0%,#d9c35a 50%,#e8e6df 100%)"></div>
  <h3>Lorem ipsum dolor sit amet, consectetur</h3>
  <div class="date"><svg width="14" height="14" viewBox="0 0 14 14"><rect x="1" y="2.5" width="12" height="10.5" rx="1.5" fill="var(--navy)"/><rect x="2.5" y="6" width="9" height="5.5" fill="#fff"/><rect x="3.5" y="0.5" width="1.6" height="3.5" fill="var(--navy)"/><rect x="8.9" y="0.5" width="1.6" height="3.5" fill="var(--navy)"/></svg>Jun 25,2025</div>
  <p>Lorem ipsum dolor sit amet, consectetur adipi scing elit, sed do eiusmod tempor incididunt ut labore et dolore magna aliqua.</p>
</article>
<article class="post" style="left:783px">
  <div class="photo" role="img" aria-label="Wooden sauna interior with a bucket and ladle" style="background:linear-gradient(160deg,#6b5a48 0%,#c9ab86 50%,#e6d4b8 100%)"></div>
  <h3>Lorem ipsum dolor sit amet, consectetur</h3>
  <div class="date"><svg width="14" height="14" viewBox="0 0 14 14"><rect x="1" y="2.5" width="12" height="10.5" rx="1.5" fill="var(--navy)"/><rect x="2.5" y="6" width="9" height="5.5" fill="#fff"/><rect x="3.5" y="0.5" width="1.6" height="3.5" fill="var(--navy)"/><rect x="8.9" y="0.5" width="1.6" height="3.5" fill="var(--navy)"/></svg>Jun 25,2025</div>
  <p>Lorem ipsum dolor sit amet, consectetur adipi scing elit, sed do eiusmod tempor incididunt ut labore et dolore magna aliqua.</p>
</article>

<!-- PILLARS -->
<section class="abs pillars"></section>
<div class="abs script center" style="top:3523px;font-size:18px;color:#fff">Pillars</div>
<h2 class="abs heading center" style="top:3553px;font-size:38px;color:#fff">OUR 4 PILLARS</h2>
<svg class="abs" style="left:500px;top:3598px" width="200" height="14" viewBox="0 0 200 14"><path d="M2 10 C 60 1, 140 1, 198 9 C 140 7, 60 7, 2 10 Z" fill="#fff"/></svg>
<div class="pillar" style="left:110px"><div class="inner">
  <svg width="100" height="100" viewBox="0 0 100 100"><rect x="47" y="6" width="6" height="40" rx="3" fill="var(--navy)"/><path d="M47 40 L36 50" stroke="var(--navy)" stroke-width="5" stroke-linecap="round"/><path d="M53 40 L64 50" stroke="var(--navy)" stroke-width="5" stroke-linecap="round"/><path d="M40 22 C 20 22, 10 55, 12 84 C 14 94, 28 92, 40 84 C 44 80, 44 40, 40 22 Z" fill="var(--navy)"/><path d="M60 22 C 80 22, 90 55, 88 84 C 86 94, 72 92, 60 84 C 56 80, 56 40, 60 22 Z" fill="var(--navy)"/></svg>
  <span>Breathe</span></div></div>
<div class="pillar" style="left:345px"><div class="inner">
  <svg width="100" height="100" viewBox="0 0 100 100"><circle cx="50" cy="16" r="10" fill="var(--navy)"/><path d="M38 32 C 44 28, 56 28, 62 32 L66 60 L80 68 L76 74 L58 66 L50 58 L42 66 L24 74 L20 68 L34 60 Z" fill="var(--navy)"/><path d="M14 82 C 30 70, 70 70, 86 82 C 70 92, 30 92, 14 82 Z" fill="var(--navy)"/></svg>
  <span>Feel</span></div></div>
<div class="pillar" style="left:582px"><div class="inner">
  <svg width="100" height="100" viewBox="0 0 100 100"><circle cx="50" cy="50" r="30" fill="none" stroke="var(--navy)" stroke-width="8"/><circle cx="50" cy="14" r="11" fill="var(--navy)"/><circle cx="19" cy="68" r="11" fill="var(--navy)"/><circle cx="81" cy="68" r="11" fill="var(--navy)"/><circle cx="50" cy="52" r="7" fill="var(--navy)"/></svg>
  <span>Connect</span></div></div>
<div class="pillar" style="left:818px"><div class="inner">
  <svg width="100" height="100" viewBox="0 0 100 100"><polygon points="50,4 54,14 65,14 56,21 59,31 50,25 41,31 44,21 35,14 46,14" fill="var(--navy)"/><polygon points="22,14 25,21 33,21 27,26 29,33 22,29 15,33 17,26 11,21 19,21" fill="var(--navy)"/><polygon points="78,14 81,21 89,21 83,26 85,33 78,29 71,33 73,26 67,21 75,21" fill="var(--navy)"/><circle cx="50" cy="50" r="12" fill="var(--navy)"/><path d="M26 92 C 26 72, 40 66, 50 66 C 60 66, 74 72, 74 92 Z" fill="var(--navy)"/></svg>
  <span>Experience</span></div></div>

<!-- CONTACT -->
<section class="abs contact"></section>
<div class="abs script center" style="top:4103px;font-size:18px">Contact Us</div>
<h2 class="abs heading center" style="top:4132px;font-size:38px">GET IN TOUCH</h2>
<svg class="abs" style="left:500px;top:4177px" width="200" height="14" viewBox="0 0 200 14"><path d="M2 10 C 60 1, 140 1, 198 9 C 140 7, 60 7, 2 10 Z" fill="var(--navy)"/></svg>

<div class="info-icon" style="top:4252px"><svg width="22" height="30" viewBox="0 0 22 30"><path d="M11 1 C 5 1, 1 5.5, 1 11 C 1 18, 11 29, 11 29 C 11 29, 21 18, 21 11 C 21 5.5, 17 1, 11 1 Z" fill="#fff"/><circle cx="11" cy="11" r="4" fill="var(--navy)"/></svg></div>
<div class="info-label" style="top:4250px">Address :</div>
<div class="info-text" style="top:4277px">Lorem ipsum dolor sit amet,<br>consectetur</div>

<div class="info-icon" style="top:4382px"><svg width="30" height="22" viewBox="0 0 30 22"><rect x="1" y="1" width="28" height="20" rx="2" fill="#fff"/><path d="M2 3 L15 13 L28 3" fill="none" stroke="var(--navy)" stroke-width="2.5"/></svg></div>
<div class="info-label" style="top:4380px">Email Address :</div>
<div class="info-text" style="top:4407px">info@companyname.com</div>

<div class="info-icon" style="top:4512px"><svg width="28" height="28" viewBox="0 0 28 28"><path d="M6 2 L11 2 L13 9 L9.5 11.5 C 11 15, 13 17, 16.5 18.5 L19 15 L26 17 L26 22 C 26 24, 24 26, 22 26 C 12 25, 3 16, 2 6 C 2 4, 4 2, 6 2 Z" fill="#fff"/></svg></div>
<div class="info-label" style="top:4510px">Phone :</div>
<div class="info-text" style="top:4537px">+1 888 888 8888</div>

<div class="field" style="left:543px;top:4233px;width:265px;height:53px">First name</div>
<div class="field" style="left:822px;top:4233px;width:266px;height:53px">Last name</div>
<div class="field" style="left:543px;top:4303px;width:265px;height:53px">Email</div>
<div class="field" style="left:822px;top:4303px;width:266px;height:53px">Phone</div>
<div class="field" style="left:543px;top:4372px;width:545px;height:158px">Message</div>
<div class="btn" style="left:543px;top:4560px;width:157px;height:38px;">SUBMIT NOW</div>

<!-- FOOTER -->
<svg class="abs" style="left:0;top:4680px" width="1200" height="80" viewBox="0 0 1200 80">
  <path d="M0 45 C 200 10, 420 10, 600 30 C 800 52, 1000 30, 1200 18 L1200 80 L0 80 Z" fill="var(--teal)"/>
  <path d="M0 58 C 180 40, 380 42, 560 52 C 800 66, 1000 48, 1200 42 L1200 80 L0 80 Z" fill="var(--navy-deep)"/>
</svg>
<footer class="abs footer"></footer>
<div class="abs f-brand"><i></i>Gather Your Light</div>
<p class="abs" style="left:145px;top:4910px;width:245px;font-size:13px;line-height:25px;color:#fff">Lorem ipsum dolor sit amet, conse ctetur adipiscing elit, sed do</p>
<div class="abs f-head" style="left:488px;top:4852px">Quick Links</div>
<ul class="abs f-links">
  <li>Home</li><li>About</li><li>Services</li><li>Reviews</li><li>Blog</li><li>Contact</li>
</ul>
<div class="abs f-head" style="left:727px;top:4852px">Subscribe to Our Newsletter</div>
<div class="abs" style="left:727px;top:4895px;width:330px;height:38px;background:#fff;border-radius:19px;font-size:13px;color:#666;padding:12px 0 0 18px">Email address</div>
<div class="btn" style="left:727px;top:4948px;width:156px;height:37px;background:var(--teal);font-size:12.5px">SUBSCRIBE</div>
<div class="abs" style="left:110px;top:5106px;width:978px;height:1px;background:rgba(255,255,255,.35)"></div>
<p class="abs center" style="top:5133px;font-size:14px;color:#fff">© Copyrights 2025 | All Rights reserved | Privacy Policy | Terms of Service</p>

</body>
</html>
```